Larkspur Ridge Management - Business Cards

I need business cards. My current logo was designed by a designer at this site and I very much like and am happy with the results. I would like a business card that is trendy, unique, current yet professional. I deal with high net worth clients daily

Target Market(s)

Out of state investors looking to get into the rental market in Ohio

Industry/Entity Type

Property Management, Consulting

Contact Information for Business Card

Name, Title (Chief Financial Officer) office phone number (555) 817-3094 website address larkridgemgmt.example

Font styles to use
Sans Serif

Colors
0054AA
0677BA
7BADD7
CADEEF
E8F1F8
0094D4
00A9DD
6FCCEA
C7EBF8
E9F6FB
00AB8E
00BBA5
67D7C9
C6EFE9
E9F9F6

```html
<!DOCTYPE html>
<html lang="en">
<head>
<meta charset="utf-8">
<title>Larkspur Ridge Management – Business Cards</title>
<link rel="stylesheet" href="https://fonts.googleapis.com/css2?family=Montserrat:wght@400;500&family=Roboto:wght@400;500&family=Ubuntu:wght@500;700&display=swap">
<style>
  :root {
    --backdrop: #2b2b2b;
    --navy: #1f2f52;
    --red: #b8232b;
    --paper-top: #f1f1f1;
    --paper-bottom: #dedede;
    --ink: #1f2f52;
    --muted: #5a5a5a;
    --white: #ffffff;
  }
  * { box-sizing: border-box; margin: 0; padding: 0; }
  html, body {
    width: 1200px; height: 1138px; overflow: hidden;
    background: var(--backdrop);
  }
  .card {
    position: absolute;
    border-radius: 16px;
    overflow: hidden;
  }
  /* Front */
  .card-front {
    left: 274px; top: 186px; width: 623px; height: 376px;
    background: var(--navy);
  }
  .brand-front {
    position: absolute; left: 0; right: 0; top: 128px;
    display: flex; flex-direction: column; align-items: center; gap: 14px;
  }
  .brand-mark {
    width: 18px; height: 18px; background: var(--red);
  }
  .brand-name {
    font-family: "Ubuntu", sans-serif; font-weight: 700;
    font-size: 34px; line-height: 1.1; text-align: center;
    text-transform: uppercase; letter-spacing: 1px;
  }
  .brand-front .brand-name { color: var(--white); }
  .front-web {
    position: absolute; left: 0; right: 0; top: 338px;
    text-align: center; color: var(--white);
    font-family: "Montserrat", sans-serif; font-size: 14px; letter-spacing: 5px;
  }
  /* Back */
  .card-back {
    left: 276px; top: 608px; width: 618px; height: 374px;
    background: linear-gradient(180deg, var(--paper-top), var(--paper-bottom));
  }
  .brand-back {
    position: absolute; left: 70px; width: 230px; top: 118px;
    display: flex; flex-direction: column; align-items: center; gap: 12px;
  }
  .brand-back .brand-name { color: var(--navy); font-size: 27px; }
  .contact {
    position: absolute; left: 352px; top: 74px;
    font-family: "Roboto", sans-serif; color: var(--ink);
  }
  .person-name {
    font-family: "Ubuntu", sans-serif; font-weight: 500;
    font-size: 26px; color: var(--red); line-height: 1;
  }
  .person-title { font-size: 17px; color: var(--muted); margin-top: 6px; }
  .address { font-size: 16px; line-height: 23px; margin-top: 14px; }
  .lines { list-style: none; margin-top: 10px; font-size: 16px; line-height: 22px; }
  .lines li { display: flex; align-items: center; gap: 13px; }
  .lines svg { width: 16px; height: 16px; flex: none; }
  .band-red {
    position: absolute; left: 0; bottom: 0; width: 290px; height: 14px;
    background: var(--red);
  }
  .band-navy {
    position: absolute; right: 0; bottom: 0; width: 354px; height: 46px;
    background: var(--navy);
    clip-path: polygon(28px 0, 100% 0, 100% 100%, 0 100%);
    display: flex; align-items: center; padding-left: 87px;
    color: var(--white); font-family: "Roboto", sans-serif; font-size: 15px;
  }
</style>
</head>
<body>
  <section class="card card-front">
    <div class="brand-front">
      <span class="brand-mark"></span>
      <div class="brand-name">Larkspur Ridge<br>Management</div>
    </div>
    <div class="front-web">www.larkridgemgmt.example</div>
  </section>

  <section class="card card-back">
    <div class="brand-back">
      <span class="brand-mark"></span>
      <div class="brand-name">Larkspur Ridge<br>Management</div>
    </div>
    <div class="contact">
      <div class="person-name">Daniel Whitmore</div>
      <div class="person-title">Chief Financial Officer</div>
      <div class="address">Street No 000, Bldg No. 0,<br>Country State - 000000</div>
      <ul class="lines">
        <li>
          <svg viewBox="0 0 16 16" aria-hidden="true"><path fill="#b8232b" d="M2 6c0-2 3-3 6-3s6 1 6 3v1h-3V5.5H5V7H2zM4 8h8l1 5H3z"/><circle cx="8" cy="10.5" r="1.4" fill="#f1f1f1"/></svg>
          (555) 817-3094
        </li>
        <li>
          <svg viewBox="0 0 16 16" aria-hidden="true"><rect x="1" y="3" width="14" height="10" fill="#b8232b"/><path d="M1 3l7 6 7-6M1 13l5-5M15 13l-5-5" stroke="#f1f1f1" stroke-width="1.2" fill="none"/></svg>
          www.larkridgemgmt.example
        </li>
        <li>
          <svg viewBox="0 0 16 16" aria-hidden="true"><circle cx="8" cy="8" r="6.5" fill="#b8232b"/><path d="M1.5 8h13M8 1.5v13M3 4.5h10M3 11.5h10M8 1.5c-3 3-3 10 0 13M8 1.5c3 3 3 10 0 13" stroke="#f1f1f1" stroke-width="0.8" fill="none"/></svg>
          info@larkridgemgmt.example
        </li>
      </ul>
    </div>
    <div class="band-red"></div>
    <div class="band-navy">Larkspur Ridge Management</div>
  </section>
</body>
</html>
```